【 概要 】 学習塾のウィンドウ(窓・入口)デザインを一新したいとの要望です。 【 依頼内容 】 ・サイズ: 別紙 ・利用用途:ウィンドウサイン、看板、ウェブサイトなど 【 デザインイメージ 】 ・ターゲット層:小中学生が通っていることが分かる事 ・参考デザイン:既存デザイン添付します ・色:現在の緑は使用したいそうです。 ・ロゴ、イメージ写真:特に指定はありません 既存のロゴを使用する場合は、デザイン上 〇〇〇〇〇 表記でお願いします 【 契約金額(税抜) 】 ¥20,000円 ※契約金額(税込)からシステム利用料を差し引いた金額が、ワーカーさまの受取金額となります その他ご質問等ありましたら、気軽にお問い合わせください。 ご応募をお待ちしております! |
この度は、ご提案有難うございました。
お客様と相談した結果、今回はTarvex様にお願いしたいと思います。
何卒宜しくお願い致します。
皆様、今回はご提案有難うございました。
あいまいな発注となっておりましたが、ご提案頂いた皆様にはご尽力いただき誠に有難うございました。
また機会がありましたら依頼させて頂きます。

```html
<!DOCTYPE html>
<html lang="ja">
<head>
<meta charset="utf-8">
<title>Window Sign Panels</title>
<link rel="stylesheet" href="https://fonts.googleapis.com/css2?family=Noto+Sans+JP:wght@500&display=swap">
<style>
  :root {
    --bg: #ffffff;
    --frame: #9a9a9a;
    --green-deep: #2b9637;
    --green-mid: #5fb546;
    --green-light: #a9d46f;
    --green-pale: #dcefc6;
    --star: #3aa845;
    --label: #ffffff;
  }
  html, body { margin: 0; padding: 0; overflow: hidden; }
  body {
    width: 1200px; height: 1104px; background: var(--bg);
    font-family: "Noto Sans JP", sans-serif; position: relative;
  }
  .defs { position: absolute; width: 0; height: 0; }
  .panel-row { position: absolute; inset: 0; }
  .window-panel { position: absolute; display: block; }
  .panel-frame { fill: #fff; stroke: var(--frame); stroke-width: 1.5; }
  .pane-divider { stroke: var(--frame); stroke-width: 1.5; }
  .wave-light { fill: var(--green-light); }
  .wave-deep { fill: var(--green-deep); }
  .wave-pale { fill: var(--green-pale); }
  .sparkle { fill: var(--star); }
  .sparkle-light { fill: var(--green-light); }
  .panel-label { fill: var(--label); font-size: 11px; letter-spacing: 1px; font-family: "Noto Sans JP", sans-serif; }
  .p1 { left: 60px;  top: 440px; width: 200px; height: 150px; }
  .p2 { left: 284px; top: 440px; width: 200px; height: 150px; }
  .p3 { left: 508px; top: 474px; width: 185px; height: 215px; }
  .p4 { left: 717px; top: 434px; width: 200px; height: 150px; }
  .p5 { left: 941px; top: 434px; width: 200px; height: 150px; }
</style>
</head>
<body>
<svg class="defs" aria-hidden="true">
  <defs>
    <symbol id="sparkle" viewBox="-10 -10 20 20">
      <path d="M0 -10 Q1.5 -1.5 10 0 Q1.5 1.5 0 10 Q-1.5 1.5 -10 0 Q-1.5 -1.5 0 -10Z"/>
    </symbol>
  </defs>
</svg>

<main class="panel-row">
  <svg class="window-panel p1" viewBox="0 0 200 150">
    <rect class="panel-frame" x="1" y="1" width="198" height="148"/>
    <path class="wave-pale" d="M1 105 Q90 125 199 95 L199 149 L1 149Z"/>
    <path class="wave-light" d="M1 112 Q100 135 199 108 L199 149 L1 149Z"/>
    <path class="wave-deep" d="M1 125 Q80 140 199 118 L199 149 L1 149Z"/>
    <line class="pane-divider" x1="100" y1="1" x2="100" y2="149"/>
    <g class="sparkle">
      <use href="#sparkle" x="28" y="20" width="9" height="9"/>
      <use href="#sparkle" x="60" y="45" width="12" height="12"/>
      <use href="#sparkle" x="40" y="72" width="8" height="8"/>
      <use href="#sparkle" x="130" y="28" width="10" height="10"/>
      <use href="#sparkle" x="160" y="60" width="13" height="13"/>
      <use href="#sparkle" x="118" y="78" width="8" height="8"/>
    </g>
    <g class="sparkle-light">
      <use href="#sparkle" x="80" y="15" width="7" height="7"/>
      <use href="#sparkle" x="175" y="20" width="7" height="7"/>
    </g>
    <text class="panel-label" x="14" y="142">〇〇〇〇〇</text>
  </svg>

  <svg class="window-panel p2" viewBox="0 0 200 150">
    <rect class="panel-frame" x="1" y="1" width="198" height="148"/>
    <path class="wave-pale" d="M1 90 Q110 120 199 70 L199 149 L1 149Z"/>
    <path class="wave-light" d="M1 110 Q110 130 199 88 L199 149 L1 149Z"/>
    <path class="wave-deep" d="M60 149 Q140 135 199 100 L199 149Z"/>
    <line class="pane-divider" x1="100" y1="1" x2="100" y2="149"/>
    <g class="sparkle">
      <use href="#sparkle" x="22" y="30" width="10" height="10"/>
      <use href="#sparkle" x="55" y="18" width="8" height="8"/>
      <use href="#sparkle" x="70" y="58" width="12" height="12"/>
      <use href="#sparkle" x="125" y="40" width="9" height="9"/>
      <use href="#sparkle" x="150" y="16" width="11" height="11"/>
      <use href="#sparkle" x="172" y="48" width="8" height="8"/>
    </g>
    <g class="sparkle-light">
      <use href="#sparkle" x="30" y="70" width="7" height="7"/>
      <use href="#sparkle" x="110" y="68" width="7" height="7"/>
    </g>
  </svg>

  <svg class="window-panel p3" viewBox="0 0 185 215">
    <rect class="panel-frame" x="1" y="1" width="183" height="213"/>
    <path class="wave-pale" d="M1 130 Q40 180 184 170 L184 214 L1 214Z"/>
    <path class="wave-light" d="M1 145 Q50 188 184 180 L184 214 L1 214Z"/>
    <path class="wave-deep" d="M1 160 Q60 200 184 192 L184 214 L1 214Z"/>
    <line class="pane-divider" x1="92.5" y1="1" x2="92.5" y2="214"/>
    <g class="sparkle">
      <use href="#sparkle" x="20" y="30" width="10" height="10"/>
      <use href="#sparkle" x="55" y="70" width="12" height="12"/>
      <use href="#sparkle" x="30" y="105" width="8" height="8"/>
      <use href="#sparkle" x="120" y="25" width="9" height="9"/>
      <use href="#sparkle" x="150" y="75" width="12" height="12"/>
      <use href="#sparkle" x="115" y="120" width="9" height="9"/>
    </g>
    <g class="sparkle-light">
      <use href="#sparkle" x="70" y="20" width="7" height="7"/>
      <use href="#sparkle" x="165" y="130" width="7" height="7"/>
    </g>
    <text class="panel-label" x="108" y="206">〇〇〇〇〇</text>
  </svg>

  <svg class="window-panel p4" viewBox="0 0 200 150">
    <rect class="panel-frame" x="1" y="1" width="198" height="148"/>
    <path class="wave-pale" d="M1 95 Q90 115 199 120 L199 149 L1 149Z"/>
    <path class="wave-light" d="M1 105 Q100 125 199 128 L199 149 L1 149Z"/>
    <path class="wave-deep" d="M1 112 Q70 135 150 149 L1 149Z"/>
    <line class="pane-divider" x1="100" y1="1" x2="100" y2="149"/>
    <g class="sparkle">
      <use href="#sparkle" x="25" y="22" width="9" height="9"/>
      <use href="#sparkle" x="62" y="48" width="12" height="12"/>
      <use href="#sparkle" x="128" y="20" width="10" height="10"/>
      <use href="#sparkle" x="165" y="42" width="12" height="12"/>
      <use href="#sparkle" x="140" y="80" width="8" height="8"/>
    </g>
    <g class="sparkle-light">
      <use href="#sparkle" x="35" y="70" width="7" height="7"/>
      <use href="#sparkle" x="85" y="25" width="7" height="7"/>
    </g>
  </svg>

  <svg class="window-panel p5" viewBox="0 0 200 150">
    <rect class="panel-frame" x="1" y="1" width="198" height="148"/>
    <path class="wave-pale" d="M1 115 Q100 95 199 100 L199 149 L1 149Z"/>
    <path class="wave-light" d="M1 125 Q110 105 199 112 L199 149 L1 149Z"/>
    <path class="wave-deep" d="M40 149 Q120 118 199 122 L199 149Z"/>
    <line class="pane-divider" x1="100" y1="1" x2="100" y2="149"/>
    <g class="sparkle">
      <use href="#sparkle" x="20" y="40" width="10" height="10"/>
      <use href="#sparkle" x="50" y="15" width="9" height="9"/>
      <use href="#sparkle" x="68" y="62" width="12" height="12"/>
      <use href="#sparkle" x="120" y="30" width="11" height="11"/>
      <use href="#sparkle" x="160" y="58" width="9" height="9"/>
      <use href="#sparkle" x="175" y="18" width="8" height="8"/>
    </g>
    <g class="sparkle-light">
      <use href="#sparkle" x="30" y="85" width="7" height="7"/>
      <use href="#sparkle" x="135" y="80" width="7" height="7"/>
    </g>
    <text class="panel-label" x="120" y="142">〇〇〇〇〇</text>
  </svg>
</main>
</body>
</html>
```